Birthday Calendar: Dec 1 - Nov 30

This calendar should have three parts. First the center should contain an annual calendar beginning December 1, 2019 and going through November 30, 2020. I'm picturing the months and date numbers - no need for individual boxes for each day. Second, above the calendar should be blank space (intended for people to write words of advise and love). Third, beneath the calendar space will be several statements about the year (i.e. "If you have client meetings four times a month, you'll meet with 36 clients." "If you kiss your kids only once each day, that's 1,460 kisses.") I don't have an exact overall size of the calendar in mind, but definitely know it will need to be bigger than 8.5"x11"

Target Market(s)

Wife - Her birthday is November 30, so this is a calendar to mark the time from one birthday to the next.

Font styles to use
Serif

Colors

Designer to choose colors to be used in the design.

Requirements
Must have
• The three different sections listed in the description. There will be 12 people handwriting simple phrases of advise (for how to have the best year) at the top, so there should be enough room for that. At the top it should say "These are the Days"
• I will provide the complete set of statements that will appear at the bottom of the calendar. There will be 10 (or less) statements total, sort of like the ones provided in the description. Let me know when you want those statements.

```html
<!DOCTYPE html>
<html lang="en">
<head>
<meta charset="utf-8">
<title>These are the Days</title>
<link rel="stylesheet" href="https://fonts.googleapis.com/css2?family=PT+Serif:wght@400;700&family=Montserrat:wght@500;600;700&display=swap">
<style>
  :root {
    --backdrop: #e8e8e8;
    --paper: #ffffff;
    --rose: #e8175d;
    --band: #ef4f76;
    --sunday: #e3132c;
    --weekday-band: #e4e4e6;
    --ink: #1f1f1f;
  }
  * { box-sizing: border-box; margin: 0; padding: 0; }
  html, body { width: 1200px; height: 1200px; overflow: hidden; background: var(--backdrop); }
  .sheet {
    position: absolute; left: 157px; top: 27px;
    width: 1108px; height: 1432px;
    transform: scale(0.8); transform-origin: 0 0;
    background: var(--paper); overflow: hidden;
  }
  .confetti {
    position: absolute; left: 0; width: 100%;
  }
  .confetti-top {
    top: 0; height: 320px;
    background: radial-gradient(ellipse at 50% 0%, rgba(240,200,215,.35), rgba(210,235,225,.2) 50%, rgba(255,255,255,0) 75%);
  }
  .confetti-bottom {
    bottom: 0; height: 330px;
    background: radial-gradient(ellipse at 50% 100%, rgba(240,190,205,.3), rgba(200,215,240,.2) 50%, rgba(255,255,255,0) 78%);
  }
  .title {
    position: absolute; left: 0; top: 44px; width: 100%;
    text-align: center;
    font-family: "PT Serif", serif; font-weight: 700;
    font-size: 72px; line-height: 1; color: var(--rose);
    text-decoration: underline; text-decoration-thickness: 3px; text-underline-offset: 6px;
  }
  .notes-space { position: absolute; left: 49px; top: 150px; width: 1010px; height: 300px; }
  .month {
    position: absolute; width: 236px;
    font-family: "Montserrat", sans-serif; color: var(--ink);
  }
  .month h2 {
    height: 24px; background: var(--band); color: #fff;
    font-size: 14px; font-weight: 600; letter-spacing: 1px;
    text-align: center; line-height: 25px;
  }
  .weekdays, .dates { display: grid; grid-template-columns: repeat(7, 1fr); text-align: center; }
  .weekdays {
    margin-top: 2px; height: 20px; background: var(--weekday-band);
    font-size: 11px; font-weight: 600; line-height: 20px;
  }
  .weekdays span:first-child { color: var(--sunday); }
  .dates { grid-auto-rows: 21.5px; font-size: 11.5px; font-weight: 500; line-height: 21.5px; }
  .dates span:nth-child(7n+1) { color: var(--sunday); font-weight: 600; }
  .col-1 { left: 49px; } .col-2 { left: 307px; } .col-3 { left: 565px; } .col-4 { left: 823px; }
  .row-1 { top: 476px; } .row-2 { top: 674px; } .row-3 { top: 872px; }
  .facts {
    position: absolute; left: 0; top: 1070px; width: 100%;
    list-style: none; text-align: center;
    font-family: "PT Serif", serif; font-size: 17.5px; line-height: 33px; color: var(--ink);
  }
  .facts strong { color: var(--rose); font-weight: 400; font-size: 20px; }
</style>
</head>
<body>
<main class="sheet">
  <div class="confetti confetti-top" role="img" aria-label="Faint scattered pastel ring confetti decoration"></div>
  <div class="confetti confetti-bottom" role="img" aria-label="Faint scattered pastel ring confetti decoration"></div>

  <h1 class="title">These are the Days</h1>
  <section class="notes-space" aria-label="Space for handwritten advice"></section>

  <section class="month col-1 row-1"><h2>DECEMBER</h2>
    <div class="weekdays"><span>S</span><span>M</span><span>T</span><span>W</span><span>T</span><span>F</span><span>S</span></div>
    <div class="dates"><span>1</span><span>2</span><span>3</span><span>4</span><span>5</span><span>6</span><span>7</span><span>8</span><span>9</span><span>10</span><span>11</span><span>12</span><span>13</span><span>14</span><span>15</span><span>16</span><span>17</span><span>18</span><span>19</span><span>20</span><span>21</span><span>22</span><span>23</span><span>24</span><span>25</span><span>26</span><span>27</span><span>28</span><span>29</span><span>30</span><span>31</span></div>
  </section>
  <section class="month col-2 row-1"><h2>JANUARY</h2>
    <div class="weekdays"><span>S</span><span>M</span><span>T</span><span>W</span><span>T</span><span>F</span><span>S</span></div>
    <div class="dates"><span></span><span></span><span></span><span>1</span><span>2</span><span>3</span><span>4</span><span>5</span><span>6</span><span>7</span><span>8</span><span>9</span><span>10</span><span>11</span><span>12</span><span>13</span><span>14</span><span>15</span><span>16</span><span>17</span><span>18</span><span>19</span><span>20</span><span>21</span><span>22</span><span>23</span><span>24</span><span>25</span><span>26</span><span>27</span><span>28</span><span>29</span><span>30</span><span>31</span></div>
  </section>
  <section class="month col-3 row-1"><h2>FEBRUARY</h2>
    <div class="weekdays"><span>S</span><span>M</span><span>T</span><span>W</span><span>T</span><span>F</span><span>S</span></div>
    <div class="dates"><span></span><span></span><span></span><span></span><span></span><span></span><span>1</span><span>2</span><span>3</span><span>4</span><span>5</span><span>6</span><span>7</span><span>8</span><span>9</span><span>10</span><span>11</span><span>12</span><span>13</span><span>14</span><span>15</span><span>16</span><span>17</span><span>18</span><span>19</span><span>20</span><span>21</span><span>22</span><span>23</span><span>24</span><span>25</span><span>26</span><span>27</span><span>28</span><span>29</span></div>
  </section>
  <section class="month col-4 row-1"><h2>MARCH</h2>
    <div class="weekdays"><span>S</span><span>M</span><span>T</span><span>W</span><span>T</span><span>F</span><span>S</span></div>
    <div class="dates"><span>1</span><span>2</span><span>3</span><span>4</span><span>5</span><span>6</span><span>7</span><span>8</span><span>9</span><span>10</span><span>11</span><span>12</span><span>13</span><span>14</span><span>15</span><span>16</span><span>17</span><span>18</span><span>19</span><span>20</span><span>21</span><span>22</span><span>23</span><span>24</span><span>25</span><span>26</span><span>27</span><span>28</span><span>29</span><span>30</span><span>31</span></div>
  </section>

  <section class="month col-1 row-2"><h2>APRIL</h2>
    <div class="weekdays"><span>S</span><span>M</span><span>T</span><span>W</span><span>T</span><span>F</span><span>S</span></div>
    <div class="dates"><span></span><span></span><span></span><span>1</span><span>2</span><span>3</span><span>4</span><span>5</span><span>6</span><span>7</span><span>8</span><span>9</span><span>10</span><span>11</span><span>12</span><span>13</span><span>14</span><span>15</span><span>16</span><span>17</span><span>18</span><span>19</span><span>20</span><span>21</span><span>22</span><span>23</span><span>24</span><span>25</span><span>26</span><span>27</span><span>28</span><span>29</span><span>30</span></div>
  </section>
  <section class="month col-2 row-2"><h2>MAY</h2>
    <div class="weekdays"><span>S</span><span>M</span><span>T</span><span>W</span><span>T</span><span>F</span><span>S</span></div>
    <div class="dates"><span></span><span></span><span></span><span></span><span></span><span>1</span><span>2</span><span>3</span><span>4</span><span>5</span><span>6</span><span>7</span><span>8</span><span>9</span><span>10</span><span>11</span><span>12</span><span>13</span><span>14</span><span>15</span><span>16</span><span>17</span><span>18</span><span>19</span><span>20</span><span>21</span><span>22</span><span>23</span><span>24</span><span>25</span><span>26</span><span>27</span><span>28</span><span>29</span><span>30</span><span>31</span></div>
  </section>
  <section class="month col-3 row-2"><h2>JUNE</h2>
    <div class="weekdays"><span>S</span><span>M</span><span>T</span><span>W</span><span>T</span><span>F</span><span>S</span></div>
    <div class="dates"><span></span><span>1</span><span>2</span><span>3</span><span>4</span><span>5</span><span>6</span><span>7</span><span>8</span><span>9</span><span>10</span><span>11</span><span>12</span><span>13</span><span>14</span><span>15</span><span>16</span><span>17</span><span>18</span><span>19</span><span>20</span><span>21</span><span>22</span><span>23</span><span>24</span><span>25</span><span>26</span><span>27</span><span>28</span><span>29</span><span>30</span></div>
  </section>
  <section class="month col-4 row-2"><h2>JULY</h2>
    <div class="weekdays"><span>S</span><span>M</span><span>T</span><span>W</span><span>T</span><span>F</span><span>S</span></div>
    <div class="dates"><span></span><span></span><span></span><span>1</span><span>2</span><span>3</span><span>4</span><span>5</span><span>6</span><span>7</span><span>8</span><span>9</span><span>10</span><span>11</span><span>12</span><span>13</span><span>14</span><span>15</span><span>16</span><span>17</span><span>18</span><span>19</span><span>20</span><span>21</span><span>22</span><span>23</span><span>24</span><span>25</span><span>26</span><span>27</span><span>28</span><span>29</span><span>30</span><span>31</span></div>
  </section>

  <section class="month col-1 row-3"><h2>AUGUST</h2>
    <div class="weekdays"><span>S</span><span>M</span><span>T</span><span>W</span><span>T</span><span>F</span><span>S</span></div>
    <div class="dates"><span></span><span></span><span></span><span></span><span></span><span></span><span>1</span><span>2</span><span>3</span><span>4</span><span>5</span><span>6</span><span>7</span><span>8</span><span>9</span><span>10</span><span>11</span><span>12</span><span>13</span><span>14</span><span>15</span><span>16</span><span>17</span><span>18</span><span>19</span><span>20</span><span>21</span><span>22</span><span>23</span><span>24</span><span>25</span><span>26</span><span>27</span><span>28</span><span>29</span><span>30</span><span>31</span></div>
  </section>
  <section class="month col-2 row-3"><h2>SEPTEMBER</h2>
    <div class="weekdays"><span>S</span><span>M</span><span>T</span><span>W</span><span>T</span><span>F</span><span>S</span></div>
    <div class="dates"><span></span><span></span><span>1</span><span>2</span><span>3</span><span>4</span><span>5</span><span>6</span><span>7</span><span>8</span><span>9</span><span>10</span><span>11</span><span>12</span><span>13</span><span>14</span><span>15</span><span>16</span><span>17</span><span>18</span><span>19</span><span>20</span><span>21</span><span>22</span><span>23</span><span>24</span><span>25</span><span>26</span><span>27</span><span>28</span><span>29</span><span>30</span></div>
  </section>
  <section class="month col-3 row-3"><h2>OCTOBER</h2>
    <div class="weekdays"><span>S</span><span>M</span><span>T</span><span>W</span><span>T</span><span>F</span><span>S</span></div>
    <div class="dates"><span></span><span></span><span></span><span></span><span>1</span><span>2</span><span>3</span><span>4</span><span>5</span><span>6</span><span>7</span><span>8</span><span>9</span><span>10</span><span>11</span><span>12</span><span>13</span><span>14</span><span>15</span><span>16</span><span>17</span><span>18</span><span>19</span><span>20</span><span>21</span><span>22</span><span>23</span><span>24</span><span>25</span><span>26</span><span>27</span><span>28</span><span>29</span><span>30</span><span>31</span></div>
  </section>
  <section class="month col-4 row-3"><h2>NOVEMBER</h2>
    <div class="weekdays"><span>S</span><span>M</span><span>T</span><span>W</span><span>T</span><span>F</span><span>S</span></div>
    <div class="dates"><span>1</span><span>2</span><span>3</span><span>4</span><span>5</span><span>6</span><span>7</span><span>8</span><span>9</span><span>10</span><span>11</span><span>12</span><span>13</span><span>14</span><span>15</span><span>16</span><span>17</span><span>18</span><span>19</span><span>20</span><span>21</span><span>22</span><span>23</span><span>24</span><span>25</span><span>26</span><span>27</span><span>28</span><span>29</span><span>30</span></div>
  </section>

  <ul class="facts">
    <li><strong>1,460</strong> – the number of kisses given if you kiss each kid just once a day.</li>
    <li><strong>12</strong> – the number of events you’ll run if you coordinate one each month.</li>
    <li><strong>52</strong> – the people you’ve made time for if you meet with just one friend each week.</li>
    <li><strong>20</strong> – about the number of dates you could go on with Morgan if you got our every few weeks.</li>
    <li><strong>260</strong> – the number of family meals shared together if you have just 5 dinners a week.</li>
    <li><strong>24</strong> – the number of cups of coffee shared with your parents if they come over twice a month.</li>
    <li><strong>156</strong> – the number of workouts you can squeeze in if you just do it three times a week.</li>
    <li><strong>4</strong> – the number of days devoted entirely to you, if you take two hours a week just for yourself.</li>
  </ul>
</main>
</body>
</html>
```